Real Estate - Property Management Prospectus/Brochure

We need a prospectus made up, around 9-10 pages including the cover page pages 3 onwards can be all a similar template happy for the front cover to have lots of black. I would like it to look very classy and futuristic, high end, blacks, silvers and whites, i am specializing in managing high end rental properties. i would like to design to correspond with the logo. I need to be able to email this booklet mostly - and also be able to print and mail out as well. I would like it crisp and clean as well - not to much on a page. Please note - happy for the cover to be simple with the logo added - prefer lots of black and with the other pages - they can all be a similar layout template to make this job easier? My website is www.leasemeridian.com.au and phone is 0491 570 156 email is hello@leasemeridian.com.au
Target Market(s)
Investors
Industry/Entity Type
Real Estate
Requirements
Should not have
- Bright greens or bold colours

```html
<!DOCTYPE html>
<html lang="en">
<head>
<meta charset="utf-8">
<title>LeaseMeridian Prospectus</title>
<link rel="stylesheet" href="https://fonts.googleapis.com/css2?family=Raleway:wght@300;400;600&display=swap">
<style>
  :root{
    --backdrop:#6d6d6d;
    --ink-black:#141414;
    --ink-mid:#2e2e2e;
    --silver:#bdbdbd;
    --silver-light:#e4e4e4;
    --white:#f5f5f5;
    --muted:#a8a8a8;
    --photo-warm-dark:#4a433d;
    --photo-warm-light:#d8d2ca;
  }
  *{box-sizing:border-box;margin:0;padding:0}
  html,body{width:809px;height:1200px;overflow:hidden}
  body{background:var(--backdrop);font-family:"Raleway",sans-serif;color:var(--white);position:relative}

  .spread{position:absolute;left:75px;width:660px;height:260px;overflow:hidden;
    background:linear-gradient(180deg,var(--ink-mid),var(--ink-black));
    box-shadow:0 6px 18px rgba(0,0,0,.35)}
  .spread::after{content:"";position:absolute;left:329.5px;top:0;width:1px;height:100%;background:rgba(255,255,255,.08)}
  .spread--cover{top:32px}
  .spread--prospectus{top:324px}
  .spread--principal{top:616px}
  .spread--why{top:908px}

  .brand{position:absolute;display:flex;align-items:center;gap:6px;font-weight:400;
    letter-spacing:.18em;text-transform:uppercase;color:var(--white)}
  .brand__mark{width:8px;height:8px;border:1px solid var(--white)}
  .brand--cover{left:400px;top:110px;width:180px;justify-content:center;font-size:10px;flex-direction:column;gap:6px}
  .brand--cover .brand__mark{width:16px;height:16px}
  .brand--page{left:22px;top:22px;font-size:13px;font-weight:600;letter-spacing:.08em;text-transform:none}

  .cover-contact{position:absolute;left:400px;top:160px;width:180px;text-align:center;
    font-size:7px;line-height:1.7;color:var(--muted);letter-spacing:.05em}

  .body-copy{position:absolute;font-size:7.5px;line-height:1.6;color:var(--silver-light);font-weight:300}
  .page-title{position:absolute;font-weight:300;font-size:15px;color:var(--white)}

  .band{position:absolute;background:linear-gradient(90deg,var(--silver),var(--silver-light))}
  .photo{position:absolute}
  .photo--towers{left:300px;top:0;width:170px;height:260px;
    clip-path:polygon(30% 0,100% 0,100% 100%,0 100%);
    background:linear-gradient(160deg,var(--photo-warm-light),#8a8178 55%,var(--photo-warm-dark))}
  .photo--model{left:205px;top:0;width:235px;height:260px;
    clip-path:polygon(40% 0,100% 0,72% 100%,0 100%);
    background:linear-gradient(170deg,#5a524b,var(--photo-warm-light) 60%,#ece8e2)}
  .photo--keys{left:345px;top:0;width:315px;height:125px;
    background:radial-gradient(ellipse at 40% 60%,var(--photo-warm-light),#7c736a 60%,var(--photo-warm-dark))}

  .ticks{list-style:none}
  .ticks li{display:flex;align-items:center;gap:5px;margin-bottom:5px}
  .ticks svg{flex:none}
  .contact-box{position:absolute;left:520px;top:150px;width:122px;border:1px solid var(--muted);padding:7px;
    font-size:6.5px;line-height:1.7;color:var(--silver-light)}
  .contact-box h3{font-size:7px;font-weight:600;letter-spacing:.1em;text-transform:uppercase;margin-bottom:4px}
</style>
</head>
<body>

<section class="spread spread--cover">
  <div class="brand brand--cover"><span class="brand__mark"></span>LeaseMeridian</div>
  <p class="cover-contact">www.leasemeridian.com.au<br>0491 570 156<br>hello@leasemeridian.com.au</p>
</section>

<section class="spread spread--prospectus">
  <div class="brand brand--page"><span class="brand__mark"></span>LeaseMeridian</div>
  <p class="body-copy" style="left:22px;top:70px;width:150px">We manage premium rental homes with care, precision and discretion, giving investors steady returns and complete peace of mind.</p>
  <div class="band" style="left:245px;top:0;width:30px;height:260px;clip-path:polygon(60% 0,100% 0,40% 100%,0 100%)"></div>
  <div class="photo photo--towers" role="img" aria-label="Photograph of a cluster of high-rise city towers"></div>
  <h2 class="page-title" style="left:495px;top:26px">Prospectus</h2>
  <p class="body-copy" style="left:495px;top:56px;width:140px">Our team brings a refined, modern approach to leasing, inspections and tenant care for high end properties.</p>
</section>

<section class="spread spread--principal">
  <div class="brand brand--page"><span class="brand__mark"></span>LeaseMeridian</div>
  <div class="band" style="left:150px;top:0;width:70px;height:260px;clip-path:polygon(70% 0,100% 0,30% 100%,0 100%);opacity:.55"></div>
  <div class="photo photo--model" role="img" aria-label="Photograph of a businessman presenting an architectural building model"></div>
  <h2 class="page-title" style="left:470px;top:26px">Principal/Broker</h2>
  <p class="body-copy" style="left:470px;top:56px;width:160px">Led by an experienced principal, every property receives personal attention, clear reporting and proactive advice.</p>
</section>

<section class="spread spread--why">
  <h2 class="page-title" style="left:22px;top:60px">Why choose us?</h2>
  <ul class="body-copy ticks" style="left:22px;top:92px;width:200px">
    <li><svg width="7" height="7" viewBox="0 0 10 10"><path d="M1 5l3 3 5-7" fill="none" stroke="#e4e4e4" stroke-width="1.5"/></svg>Dedicated property manager</li>
    <li><svg width="7" height="7" viewBox="0 0 10 10"><path d="M1 5l3 3 5-7" fill="none" stroke="#e4e4e4" stroke-width="1.5"/></svg>Thorough tenant screening</li>
    <li><svg width="7" height="7" viewBox="0 0 10 10"><path d="M1 5l3 3 5-7" fill="none" stroke="#e4e4e4" stroke-width="1.5"/></svg>Monthly owner statements</li>
    <li><svg width="7" height="7" viewBox="0 0 10 10"><path d="M1 5l3 3 5-7" fill="none" stroke="#e4e4e4" stroke-width="1.5"/></svg>Fast maintenance response</li>
  </ul>
  <div class="photo photo--keys" role="img" aria-label="Photograph of keys being handed over between two hands"></div>
  <p class="body-copy" style="left:360px;top:150px;width:140px">Your investment deserves expert hands and a service built around you.</p>
  <div class="contact-box">
    <h3>Contact details</h3>
    www.leasemeridian.com.au<br>0491 570 156<br>hello@leasemeridian.com.au
  </div>
</section>

</body>
</html>
```